Real Estate Brokerage Stationery Designs

I am looking to have presentation folders with business card slots on both sides along with pockets on both sides. I've attached logos, website colors along with current business card designs.

I am looking for envelope designs both big and small. Possibly new business card designs, notepad templates for big and small notepads. Letterhead designs. Pop socket designs. Realtors name badge designs.

www.tallbrookhomes.example

```html
<!DOCTYPE html>
<html lang="en">
<head>
<meta charset="utf-8">
<title>Tallbrook Homes – Business Card</title>
<link href="https://fonts.googleapis.com/css2?family=Roboto:wght@400;500;700&display=swap" rel="stylesheet">
<style>
  :root {
    --backdrop: #e6e6e6;
    --card: #ffffff;
    --brand-blue: #0a56a8;
    --ink: #1e1e1e;
    --text-grey: #444444;
    --muted: #6a6a6a;
    --skyline-grey: #c4c4c4;
    --photo-tone: #3a3a3a;
  }
  * { margin: 0; padding: 0; box-sizing: border-box; }
  html, body { width: 1133px; height: 1200px; overflow: hidden; }
  body {
    background: var(--backdrop);
    font-family: "Roboto", Arial, sans-serif;
    position: relative;
  }
  .card {
    position: absolute;
    width: 697px;
    height: 398px;
    background: var(--card);
    overflow: hidden;
  }
  .card--front { left: 219px; top: 153px; }
  .card--back { left: 216px; top: 647px; }

  .portrait {
    position: absolute; left: 38px; top: 35px; width: 90px; height: 105px;
    border-radius: 8px; border: 1px solid #bdbdbd;
    background: linear-gradient(180deg, #e9e9e9 0%, #9a9a9a 55%, var(--photo-tone) 100%);
  }
  .agent-name {
    position: absolute; left: 38px; top: 150px;
    font-size: 26px; font-weight: 700; color: var(--brand-blue);
  }
  .agent-title {
    position: absolute; left: 38px; top: 181px;
    font-size: 17px; font-weight: 500; color: var(--ink);
  }
  .office-address {
    position: absolute; left: 38px; top: 210px;
    font-size: 16px; line-height: 21px; color: var(--text-grey);
  }
  .contact-list {
    position: absolute; left: 38px; top: 262px; list-style: none;
    font-size: 16px; color: var(--text-grey);
  }
  .contact-list li { display: flex; align-items: center; height: 22px; }
  .contact-list svg { width: 16px; height: 16px; margin-right: 12px; fill: var(--brand-blue); }
  .skyline-art {
    position: absolute; left: 334px; top: 60px; width: 363px; height: 305px;
    background: linear-gradient(160deg, var(--skyline-grey) 0%, #6f8fc0 45%, var(--brand-blue) 100%);
  }
  .web-band {
    position: absolute; left: 0; bottom: 0; width: 100%; height: 32px;
    background: var(--brand-blue);
    color: #fff; font-size: 15px; letter-spacing: 8.3px;
    padding-left: 40px; line-height: 33px;
  }

  .brand-lockup {
    position: absolute; left: 0; top: 170px; width: 100%;
    display: flex; justify-content: center; align-items: center; gap: 12px;
  }
  .brand-mark { width: 18px; height: 18px; background: var(--brand-blue); }
  .brand-name { font-size: 38px; font-weight: 500; color: var(--ink); }
  .services {
    position: absolute; left: 0; top: 325px; width: 100%;
    text-align: center; font-size: 17px; line-height: 22px; color: var(--muted);
  }
  .services .dot {
    display: inline-block; width: 6px; height: 6px; background: var(--brand-blue);
    vertical-align: middle; margin: 0 5px;
  }
  .badge { position: absolute; border: 2px solid var(--ink); }
  .badge--housing { left: 24px; top: 332px; width: 53px; height: 50px; }
  .badge--listing { left: 588px; top: 328px; width: 83px; height: 41px; }
</style>
</head>
<body>
  <section class="card card--front">
    <div class="portrait" role="img" aria-label="Portrait photo of the broker"></div>
    <h1 class="agent-name">MarcusDelane</h1>
    <p class="agent-title">Broker</p>
    <p class="office-address">2840 Harbor Crest Ave, Suite 410,<br>Lakeview Shores, FL 33900</p>
    <ul class="contact-list">
      <li><svg viewBox="0 0 24 24"><path d="M6.6 10.8a15 15 0 0 0 6.6 6.6l2.2-2.2a1 1 0 0 1 1-.25 11.4 11.4 0 0 0 3.6.6 1 1 0 0 1 1 1V20a1 1 0 0 1-1 1A17 17 0 0 1 3 4a1 1 0 0 1 1-1h3.5a1 1 0 0 1 1 1c0 1.25.2 2.45.6 3.6a1 1 0 0 1-.25 1z"/></svg>555-210-4812</li>
      <li><svg viewBox="0 0 24 24"><path d="M7 1h10a2 2 0 0 1 2 2v18a2 2 0 0 1-2 2H7a2 2 0 0 1-2-2V3a2 2 0 0 1 2-2zm0 3v14h10V4z"/></svg>555-384-1907</li>
      <li><svg viewBox="0 0 24 24"><path d="M7 2h8l3 3v5H7zM3 11h18a1 1 0 0 1 1 1v7a1 1 0 0 1-1 1H3a1 1 0 0 1-1-1v-7a1 1 0 0 1 1-1zm3 3v2h8v-2z"/></svg>555-672-3318</li>
      <li><svg viewBox="0 0 24 24"><path d="M2 5h20v14H2zm2 2v.5l8 5.5 8-5.5V7l-8 5.5z"/></svg>marcus@tallbrookhomes.example</li>
    </ul>
    <div class="skyline-art" role="img" aria-label="Decorative city skyline and rooftops illustration"></div>
    <div class="web-band">www.tallbrookhomes.example</div>
  </section>

  <section class="card card--back">
    <div class="brand-lockup">
      <span class="brand-mark"></span>
      <span class="brand-name">Tallbrook Homes</span>
    </div>
    <p class="services">
      Esidential Real Estate <span class="dot"></span> CommercialReal Estate<br>
      Property Management <span class="dot"></span> Investments
    </p>
    <div class="badge badge--housing" aria-label="Housing badge"></div>
    <div class="badge badge--listing" aria-label="Listing service badge"></div>
  </section>
</body>
</html>
```